Managed IT services business card design

We haven't needed a business card since the founding of the business in 2005. All our clients have been coming through word of mouth. And lately more and more existing clients are requesting for our business cards to pass on to their contacts in recommending us.
So we needing a business card design. We use various innovative solutions and methodologies to provide IT services to small businesses in managing their IT systems. Our role is the same as an in-house, full-time IT Manager for our clients, but outsourced. So we take care of all our clients' IT needs, just as an IT Manager would be expected to perform.
We have a holding website, which we're happy to leave for now. If we can use the same logo would be great - www.lomvex.com.au
Preferred colours are shades of are white, grey and black.
We pride our business with the following traits: proactive, good service, prompt response, trustworthy.
Target Market(s)
Small businesses of any industry
Industry/Entity Type
Business

```html
<!DOCTYPE html>
<html lang="en">
<head>
<meta charset="utf-8">
<title>Lomvex business card</title>
<link rel="stylesheet" href="https://fonts.googleapis.com/css2?family=Exo+2:wght@400;500&display=swap">
<style>
  :root {
    --page-bg: #e6e4e1;
    --card-dark: #363536;
    --card-light-start: #fafafa;
    --card-light-end: #e2e2e2;
    --crescent: #a9a9ab;
    --text-light: #ffffff;
    --logo-ink: #3c3c3c;
  }
  * { margin: 0; padding: 0; box-sizing: border-box; }
  html, body { width: 1200px; height: 900px; overflow: hidden; }
  body {
    background: var(--page-bg);
    font-family: "Exo 2", "Segoe UI", sans-serif;
    position: relative;
  }
  .card {
    position: absolute;
    left: 75px; top: 150px;
    width: 1050px; height: 600px;
    overflow: hidden;
    box-shadow: 0 12px 30px rgba(0,0,0,0.25);
  }
  .card-shapes { position: absolute; inset: 0; }
  .contact-block {
    position: absolute;
    left: 90px; top: 62px;
    color: var(--text-light);
  }
  .person-name {
    font-size: 32px; font-weight: 500;
    letter-spacing: 0.06em; text-transform: uppercase;
  }
  .person-role { font-size: 21px; margin-top: 4px; letter-spacing: 0.03em; }
  .address { font-size: 21px; line-height: 30px; margin-top: 40px; letter-spacing: 0.04em; }
  .contact-list { list-style: none; margin-top: 48px; }
  .contact-item {
    display: flex; align-items: center; gap: 16px;
    font-size: 19px; letter-spacing: 0.08em; height: 36px;
  }
  .contact-item.small { font-size: 16px; letter-spacing: 0.04em; }
  .contact-icon { width: 20px; height: 20px; flex: none; fill: var(--text-light); }
  .brand-name {
    position: absolute;
    left: 600px; top: 255px;
    font-size: 80px; font-weight: 500;
    letter-spacing: 0.26em;
    color: var(--logo-ink);
  }
</style>
</head>
<body>
  <div class="card">
    <svg class="card-shapes" viewBox="0 0 1050 600" width="1050" height="600">
      <defs>
        <linearGradient id="lightPanel" x1="0" y1="0" x2="1" y2="1">
          <stop offset="0" stop-color="var(--card-light-start)"/>
          <stop offset="1" stop-color="var(--card-light-end)"/>
        </linearGradient>
      </defs>
      <rect class="dark-panel" width="1050" height="600" fill="var(--card-dark)"/>
      <path class="crescent" d="M 640 0 C 480 80, 400 340, 470 600 L 480 600 C 428 340, 500 95, 658 0 Z" fill="var(--crescent)"/>
      <path class="light-panel" d="M 680 0 C 530 70, 440 330, 505 600 L 1050 600 L 1050 0 Z" fill="url(#lightPanel)"/>
    </svg>

    <div class="contact-block">
      <p class="person-name">Daniel Marsh</p>
      <p class="person-role">Managing Director</p>
      <p class="address">42 Level 5, Harbour<br>Road NSW</p>
      <ul class="contact-list">
        <li class="contact-item">
          <svg class="contact-icon" viewBox="0 0 24 24"><path d="M6.6 10.8c1.4 2.8 3.8 5.1 6.6 6.6l2.2-2.2c.3-.3.7-.4 1-.2 1.1.4 2.3.6 3.6.6.6 0 1 .4 1 1V20c0 .6-.4 1-1 1C10.6 21 3 13.4 3 4c0-.6.4-1 1-1h3.5c.6 0 1 .4 1 1 0 1.3.2 2.5.6 3.6.1.3 0 .7-.2 1z"/></svg>
          02 8123 4501
        </li>
        <li class="contact-item">
          <svg class="contact-icon" viewBox="0 0 24 24"><path d="M7 1h10a2 2 0 0 1 2 2v18a2 2 0 0 1-2 2H7a2 2 0 0 1-2-2V3a2 2 0 0 1 2-2zm0 3v14h10V4zm5 15.5a1 1 0 1 0 0 2 1 1 0 0 0 0-2z"/></svg>
          0412 555 830
        </li>
        <li class="contact-item">
          <svg class="contact-icon" viewBox="0 0 24 24"><path d="M4 2h10v20H4zm2 3v2h2V5zm4 0v2h2V5zM6 9v2h2V9zm4 0v2h2V9zm-4 4v2h2v-2zm4 0v2h2v-2zm6-5h4v14h-4z"/></svg>
          02 8123 4599
        </li>
        <li class="contact-item small">
          <svg class="contact-icon" viewBox="0 0 24 24"><path d="M2 5h20v14H2zm2 2v.5l8 5 8-5V7zm0 3v7h16v-7l-8 5z"/></svg>
          daniel@lomvex.com.au
        </li>
        <li class="contact-item small">
          <svg class="contact-icon" viewBox="0 0 24 24"><path d="M12 2a10 10 0 1 0 0 20 10 10 0 0 0 0-20zm6.9 6h-3a15 15 0 0 0-1.4-3.6A8 8 0 0 1 18.9 8zM12 4c.8 1.2 1.5 2.5 1.9 4h-3.8c.4-1.5 1.1-2.8 1.9-4zM4.3 14a8 8 0 0 1 0-4h3.4a16 16 0 0 0 0 4zm.8 2h3a15 15 0 0 0 1.4 3.6A8 8 0 0 1 5.1 16zm3-8h-3a8 8 0 0 1 4.4-3.6A15 15 0 0 0 8.1 8zM12 20c-.8-1.2-1.5-2.5-1.9-4h3.8c-.4 1.5-1.1 2.8-1.9 4zm2.3-6H9.7a14 14 0 0 1 0-4h4.6a14 14 0 0 1 0 4zm.2 5.6a15 15 0 0 0 1.4-3.6h3a8 8 0 0 1-4.4 3.6zm1.8-5.6a16 16 0 0 0 0-4h3.4a8 8 0 0 1 0 4z"/></svg>
          www.lomvex.com.au
        </li>
      </ul>
    </div>

    <p class="brand-name">lomvex</p>
  </div>
</body>
</html>
```